Medical equipment business looking for professional, unique business card

We need a business card design for a durable medical equipment company. We are small but would like our cards to express that we are much bigger. We focus on braces (back, knee, wrist, etc) but also do crutches, rollators, wheelchairs- basically medical equipment that gets you going and back in Action. Our colors are blue and green and our logo has an arrow and use of a "spine". We'd like to express professionalism while being unique.

Industry/Entity Type

Medical Equipment

Contact Information for Business Card

Professional feel but unique. Memorable.

Font styles to use
Serif
Sans Serif
Other font styles liked:
• verdana

Requirements
Must have
• card holders cell#, business phone#, fax#, email, website address, business address, logo
Nice to have
• use of medical/healthcare related descriptive words, items, look
Should not have
• the wrong colors or cartoon characters.

```html
<!DOCTYPE html>
<html lang="en">
<head>
<meta charset="utf-8">
<title>Stride DME – Business Card</title>
<link rel="stylesheet" href="https://fonts.googleapis.com/css2?family=Roboto:wght@400;500&family=Open+Sans:wght@600&display=swap">
<style>
  :root {
    --navy: #0f4a6e;
    --sky: #1f8fc9;
    --lime: #8cc63f;
    --ink: #123f5c;
    --paper: #ffffff;
    --backdrop: #e9ecef;
  }
  * { box-sizing: border-box; margin: 0; padding: 0; }
  html, body { width: 900px; height: 1200px; overflow: hidden; }
  body {
    background: var(--backdrop);
    font-family: "Roboto", Arial, sans-serif;
    position: relative;
  }
  .card {
    position: absolute;
    left: 92px; top: 400px;
    width: 716px; height: 412px;
    background: var(--paper);
    border-radius: 24px;
    box-shadow: 0 6px 18px rgba(0,0,0,0.18);
    overflow: hidden;
  }
  .brand-artwork {
    position: absolute;
    right: 0; top: 0;
    width: 380px; height: 412px;
    background:
      linear-gradient(100deg, rgba(255,255,255,1) 0%, rgba(255,255,255,0) 38%),
      linear-gradient(160deg, rgba(31,143,201,0.35) 0%, rgba(140,198,63,0.55) 45%, rgba(15,74,110,0.85) 100%);
  }
  .brand {
    position: absolute;
    left: 44px; top: 58px;
    display: flex; align-items: center; gap: 14px;
  }
  .brand-dot {
    width: 22px; height: 22px; border-radius: 50%;
    background: var(--lime);
  }
  .brand-name {
    font-family: "Open Sans", Arial, sans-serif;
    font-weight: 600;
    font-size: 46px;
    line-height: 1;
    color: var(--navy);
    letter-spacing: 0.5px;
  }
  .tagline {
    position: absolute;
    left: 151px; top: 127px;
    font-family: "Open Sans", Arial, sans-serif;
    font-weight: 600;
    font-size: 17px;
    color: var(--sky);
  }
  .tagline-rule {
    position: absolute;
    left: 152px; top: 119px;
    width: 254px; height: 2px;
    background: linear-gradient(90deg, rgba(140,198,63,0), var(--lime));
  }
  .holder { position: absolute; left: 40px; top: 194px; }
  .holder-name {
    font-size: 27px; font-weight: 500; color: var(--ink); line-height: 1.1;
  }
  .holder-role {
    font-size: 15px; font-weight: 500; color: var(--lime); margin-top: 4px;
  }
  .address {
    position: absolute; left: 40px; top: 252px;
    font-size: 15px; line-height: 21px; color: var(--ink);
    font-style: normal;
  }
  .contacts {
    position: absolute; left: 40px; top: 300px;
    list-style: none;
    font-size: 15px; color: var(--ink);
  }
  .contacts li {
    display: flex; align-items: center; gap: 7px; height: 21px;
  }
  .contacts svg { width: 14px; height: 14px; flex: none; }
</style>
</head>
<body>
  <main class="card">
    <div class="brand-artwork" role="img" aria-label="Large decorative brand symbol in navy, green and blue"></div>

    <div class="brand">
      <span class="brand-dot"></span>
      <span class="brand-name">Stride DME</span>
    </div>
    <div class="tagline-rule"></div>
    <p class="tagline">Durable Medical Equipment</p>

    <section class="holder">
      <h1 class="holder-name">Laura Bennett</h1>
      <p class="holder-role">Director Operations</p>
    </section>

    <address class="address">
      418 Harbor Street<br>Portland 40127
    </address>

    <ul class="contacts">
      <li>
        <svg viewBox="0 0 14 14" aria-hidden="true"><rect x="3" y="1" width="8" height="12" rx="1.5" fill="none" stroke="#8cc63f" stroke-width="1.6"/><rect x="5.5" y="10.3" width="3" height="1.2" fill="#8cc63f"/></svg>
        061-572-208
      </li>
      <li>
        <svg viewBox="0 0 14 14" aria-hidden="true"><path d="M3 1.5l2.3 0.4 0.9 2.8-1.6 1.2a7 7 0 0 0 3.5 3.5l1.2-1.6 2.8 0.9 0.4 2.3c-0.3 0.9-1.2 1.5-2.2 1.4A10 10 0 0 1 1.6 3.7C1.5 2.7 2.1 1.8 3 1.5z" fill="#8cc63f"/></svg>
        318-590-216
      </li>
      <li>
        <svg viewBox="0 0 14 14" aria-hidden="true"><rect x="1" y="3" width="12" height="8.5" rx="1" fill="#8cc63f"/><path d="M1.5 3.6L7 8l5.5-4.4" fill="none" stroke="#fff" stroke-width="1.2"/></svg>
        hello@stridedme.com
      </li>
      <li>
        <svg viewBox="0 0 14 14" aria-hidden="true"><rect x="1" y="2" width="12" height="8.5" rx="1" fill="none" stroke="#8cc63f" stroke-width="1.6"/><rect x="5" y="11.5" width="4" height="1.5" fill="#8cc63f"/></svg>
        www.stridedme.com.au
      </li>
    </ul>
  </main>
</body>
</html>
```